Lumen Business Cards

We need a new look business cvard to refelect our new look website www.lumenplan.com.au
We’re Lumen, a team of town planning and traffic and transport engineering specialists located in Melbourne.

Lumen is a company that is structured, articulate, dynamic, progressive, accurate and adaptable.
Our key messages are:
1. We make your life easier by doing what we do best
2. We tell you what you need to know not what you want to hear
3. Polished and professional but not afraid to show some personality

we would like a bold new look that is polished and professional but not afraid to show a bit of personality

Target Market(s)

Lumen’s diverse client base consists of architecture practices, builders, developers, local government and the legal fraternity.

Industry/Entity Type

Town

Requirements
Must have
• must use our logo and have the following information

Joel Petrakis
Director

Lumen Advisory Pty Ltd
Hillgate first floor
Cotter Street
Kewdale VIC 3187 Australia
+61 03 9581 6724
mail@lumenplan.com.au
www.lumenplan.com.au
Nice to have
• We would like to see the logo used or the colours of the logo used.

```html
<!DOCTYPE html>
<html lang="en">
<head>
<meta charset="utf-8">
<title>Lumen Business Cards</title>
<link href="https://fonts.googleapis.com/css2?family=Open+Sans:wght@400;600;700&display=swap" rel="stylesheet">
<style>
  :root {
    --backdrop: #e9e7e3;
    --card: #ffffff;
    --slate: #505a66;
    --slate-light: #8c949e;
    --ink: #3f4852;
    --ink-soft: #6b737c;
    --accent: #3d9a4a;
    --on-slate: #f3f5f7;
  }
  * { box-sizing: border-box; margin: 0; padding: 0; }
  html, body {
    width: 1200px; height: 720px; overflow: hidden;
    background: var(--backdrop);
    font-family: "Open Sans", Arial, sans-serif;
  }
  .canvas { position: relative; width: 1200px; height: 720px; }
  .card {
    position: absolute; top: 205px;
    width: 540px; height: 309px;
    background: var(--card);
    box-shadow: 0 6px 18px rgba(0,0,0,0.18);
    overflow: hidden;
  }
  .card--front { left: 40px; }
  .card--back { left: 620px; }

  .front-band { position: absolute; inset: 0; }

  .holder { position: absolute; top: 26px; right: 150px; text-align: right; }
  .holder__name { font-weight: 700; font-size: 17px; color: var(--ink); }
  .holder__role { font-size: 12px; color: var(--ink-soft); margin-top: 1px; }

  .wordmark {
    position: absolute; left: 34px; top: 128px;
    display: flex; align-items: center; gap: 10px;
  }
  .wordmark__square { width: 14px; height: 14px; background: var(--accent); }
  .wordmark__name {
    font-weight: 400; font-size: 52px; letter-spacing: 1px;
    color: var(--ink); line-height: 1;
  }

  .address {
    position: absolute; left: 36px; top: 212px;
    font-size: 12.5px; line-height: 1.4; color: var(--ink);
  }
  .address__company { font-weight: 700; }

  .contact {
    position: absolute; right: 28px; top: 150px;
    list-style: none; color: var(--on-slate); font-size: 12.5px;
  }
  .contact li { display: flex; align-items: center; gap: 8px; margin-bottom: 6px; }
  .contact svg { width: 12px; height: 12px; flex: none; }

  .back-mark {
    position: absolute; left: 0; right: 0; top: 78px;
    text-align: center;
    font-weight: 400; font-size: 120px; letter-spacing: 4px;
    color: var(--slate); line-height: 1;
  }
  .back-web {
    position: absolute; left: 0; right: 0; bottom: 40px;
    text-align: center; font-size: 14px; letter-spacing: 3px;
    color: var(--ink);
  }
</style>
</head>
<body>
<main class="canvas">

  <section class="card card--front" aria-label="Business card front">
    <svg class="front-band" viewBox="0 0 540 309" preserveAspectRatio="none" aria-hidden="true">
      <path d="M392 0 L540 0 L540 309 L150 309 C300 250 430 150 392 0 Z" fill="var(--slate-light)"/>
      <path d="M412 0 L540 0 L540 309 L178 309 C320 250 448 150 412 0 Z" fill="var(--slate)"/>
    </svg>

    <div class="holder">
      <p class="holder__name">Joel Petrakis</p>
      <p class="holder__role">Director</p>
    </div>

    <div class="wordmark">
      <span class="wordmark__square"></span>
      <span class="wordmark__name">lumen</span>
    </div>

    <address class="address" style="font-style:normal">
      <p class="address__company">Lumen Advisory Pty Ltd</p>
      <p>Hillgate first floor, Cotter Street</p>
      <p>Kewdale VIC 3187 Australia</p>
    </address>

    <ul class="contact">
      <li>
        <svg viewBox="0 0 12 12" aria-hidden="true"><circle cx="6" cy="6" r="5.5" fill="none" stroke="currentColor"/><path d="M4 3.5 L5 3.5 L5.5 5 L4.8 5.6 Q5.6 7 6.6 7.4 L7.2 6.7 L8.6 7.2 L8.6 8.2 Q5 8.8 4 3.5Z" fill="currentColor"/></svg>
        <span>+61 03 9581 6724</span>
      </li>
      <li>
        <svg viewBox="0 0 12 12" aria-hidden="true"><rect x="1" y="3" width="10" height="7" fill="none" stroke="currentColor"/><path d="M1 3 L6 7 L11 3" fill="none" stroke="currentColor"/></svg>
        <span>mail@lumenplan.com.au</span>
      </li>
      <li>
        <svg viewBox="0 0 12 12" aria-hidden="true"><circle cx="6" cy="6" r="5" fill="none" stroke="currentColor"/><ellipse cx="6" cy="6" rx="2.2" ry="5" fill="none" stroke="currentColor"/><path d="M1 6 H11" stroke="currentColor"/></svg>
        <span>www.lumenplan.com.au</span>
      </li>
    </ul>
  </section>

  <section class="card card--back" aria-label="Business card back">
    <p class="back-mark">lumen</p>
    <p class="back-web">www.lumenplan.com.au</p>
  </section>

</main>
</body>
</html>
```